Kestrel Bay Warehousing Group Needs A Website

We are looking for a website for a new company. 4 Pages

Needs to be responsive and mobile friendly for all browsers and coded for both Android & IOS. SEO is also important.

Website Brief – Kestrel Bay Warehousing Group
Domain: www.kestrelbaywarehousing.com
Email: info@kestrelbaywarehousing.com
Phone: to be inserted later
Address: 10458 82 Ave, Edmonton, AB T6E 2K9
Platform: WordPress (recommended for flexibility, SEO tools, and ease of editing)
Requirements:
• Responsive & mobile-friendly (Android & iOS)
• Cross-browser compatibility
• Fast page load speed
• SEO optimized for storage development, management, and investment keywords
• Easy in-house editing after launch
• Professional, modern, trust-driven design reflecting expertise, reliability, and innovation
________________________________________
Pages
1. HOME
Purpose: Quickly communicate who Kestrel Bay Warehousing Group is and why they’re the best choice for designing, building, leasing, and managing self storage facilities.
Content Highlights:
• Hero Section: Large, bold image of a modern self storage facility with headline:
"From Concept to Capacity – Your Self Storage Experts"
• Subheadline: “Kestrel Bay Warehousing Group delivers turnkey design, construction, leasing, and management services for profitable self storage operations.”
• Quick Service Icons:
o Facility Design & Development
o Construction & Build Management
o Lease-Up & Marketing
o Ongoing Facility Management
• Call to Action Button: “LEARN MORE” → links to ABOUT US page.
• Featured Project Highlights: Showcase a few completed or current projects with photos and stats.
• Contact Banner: “Ready to build your next self storage project? Let’s talk.” → CONTACT page.
2. ABOUT US
Purpose: Build credibility, showcase experience, and explain the value proposition.
Content Highlights:
• Who We Are: Overview of Kestrel Bay Warehousing Group’ history, mission, and team expertise.
• Our Approach: End-to-end process from site selection to occupancy.
• Why Choose Us:
o Industry expertise in self storage
o Proven track record in lease-up success
o Strong vendor and contractor network
3. SERVICES
Purpose: Detail all service offerings with clarity and authority.
Sections:
• Design & Development: Market analysis, site planning, and architectural design.
• Construction Management: Overseeing timelines, budgets, and quality control.
• Lease-Up Strategy: Marketing, promotions, and occupancy acceleration.
• Ongoing Facility Management: Staffing, maintenance, revenue optimization.

4. CONTACT
Purpose: Provide simple, direct ways to connect.
Content Highlights:
• Contact Form (Name, Email, Phone, Message)
• Direct Email: info@kestrelbaywarehousing.com
• Phone (if applicable)
• Google Map embed (if there’s a head office location)
• CTA: “Let’s Build Your Storage Success Story.”
Design & Technical Notes
• Visual Style: Clean, modern, bold typography, professional color palette (to be based on branding), strong imagery of self storage facilities.
• Performance: Image compression, caching, responsive scaling.
• SEO Targets: “Self storage facility developer,” “self storage construction,” “self storage management company,” “lease-up services for self storage.”

WordPress or Joomla – must be desktop and mobile friendly with fast page load speed. Need the ability to edit ourselves.

Use pantone colours - #033c5a – dark blue
#2baadf – light blue

```html
<!DOCTYPE html>
<html lang="en">
<head>
<meta charset="utf-8">
<title>Kestrel Bay Warehousing Group – Self Storage Experts</title>
<link rel="stylesheet" href="https://fonts.googleapis.com/css2?family=Poppins:wght@400;500;600;700&family=Lato:wght@400;700&display=swap">
<style>
:root{
  --dark-blue:#033c5a;
  --light-blue:#2baadf;
  --btn-blue:#1f9bd7;
  --charcoal:#3a3a3a;
  --charcoal-deep:#333333;
  --ink:#222222;
  --muted:#555555;
  --white:#ffffff;
}
*{box-sizing:border-box;margin:0;padding:0}
html,body{width:1200px;height:3360px;overflow:hidden}
body{position:relative;font-family:'Lato',sans-serif;color:var(--ink);background:var(--white)}
.backdrop{position:absolute;left:0;top:0;width:1200px;height:3360px}
.abs{position:absolute}
.btn{position:absolute;display:flex;align-items:center;justify-content:center;background:linear-gradient(180deg,#2fb1e6,#1992cf);color:var(--white);font-family:'Poppins',sans-serif;font-size:15px;letter-spacing:.2px;border-radius:5px;text-decoration:none;box-shadow:0 3px 8px rgba(0,0,0,.15)}
/* header */
.site-header{position:absolute;left:0;top:0;width:1200px;height:91px;background:var(--white);border-bottom:3px solid var(--light-blue)}
.brand{position:absolute;display:flex;align-items:center;gap:10px;font-family:'Poppins',sans-serif;font-weight:600;font-size:18px;color:var(--dark-blue)}
.brand-mark{width:26px;height:26px;background:var(--light-blue)}
.main-nav a{position:absolute;top:38px;font-family:'Poppins',sans-serif;font-size:15px;color:#333;text-decoration:none}
.main-nav a.active{color:var(--light-blue);font-weight:600}
/* hero */
.hero-title{left:113px;top:200px;width:520px;font-family:'Poppins',sans-serif;font-weight:700;font-size:47px;line-height:52px;color:var(--white)}
.hero-text{left:112px;top:382px;width:460px;font-size:18.5px;line-height:28px;color:var(--white)}
/* sections */
.eyebrow{position:absolute;left:0;width:1200px;text-align:center;font-family:'Poppins',sans-serif;font-size:13px;color:var(--light-blue);letter-spacing:.3px}
.section-title{position:absolute;left:0;width:1200px;text-align:center;font-family:'Poppins',sans-serif;font-weight:700;font-size:42px;color:var(--ink)}
.section-title .accent{color:var(--light-blue)}
.service-card{position:absolute;top:902px;width:286px;height:287px;background:var(--white);box-shadow:0 4px 18px rgba(0,0,0,.08);text-align:center}
.service-card.active{background:var(--btn-blue);box-shadow:none}
.service-card.active::after{content:"";position:absolute;inset:11px;border:2px solid rgba(255,255,255,.9)}
.service-icon{width:92px;height:73px;margin:38px auto 0;background:var(--btn-blue);display:flex;align-items:center;justify-content:center}
.service-card.active .service-icon{background:var(--white)}
.service-card h3{margin-top:22px;font-family:'Poppins',sans-serif;font-weight:400;font-size:19px;line-height:26px;color:#333}
.service-card.active h3{color:var(--white)}
.service-card p{margin:16px auto 0;width:240px;font-size:13px;line-height:20px;color:#555}
.service-card.active p{color:var(--white)}
/* projects */
.project-card{position:absolute;width:465px;height:319px;border:3px solid var(--white);overflow:hidden}
.project-photo{position:absolute;inset:0}
.project-label{position:absolute;left:0;top:230px;width:411px;height:52px;background:var(--white);display:flex;align-items:center;padding-left:22px;gap:14px;font-family:'Poppins',sans-serif;font-size:17px;color:#333}
.project-details{position:absolute;left:2px;top:92px;width:412px;height:210px;background:rgba(31,155,215,.93);padding:14px}
.project-details .frame{border:2px solid rgba(255,255,255,.9);height:100%;padding:16px 14px 0;color:var(--white);font-family:'Poppins',sans-serif}
.project-details h4{font-weight:600;font-size:16px;margin-bottom:10px}
.project-details li{list-style:none;font-size:14px;line-height:28.5px;display:flex;align-items:center;gap:6px;white-space:nowrap}
/* contact */
.cta-title{left:0;top:2560px;width:1200px;text-align:center;font-family:'Poppins',sans-serif;font-weight:700;font-size:42px;line-height:51px;color:var(--ink)}
.cta-title .accent{color:var(--light-blue)}
.cta-text{left:0;top:2688px;width:1200px;text-align:center;font-size:18px;line-height:28px;color:#444}
/* footer */
.footer-rule{position:absolute;left:0;width:1200px;height:1px;background:#5a5a5a}
.footer-nav{position:absolute;left:0;top:3096px;width:1200px;display:flex;justify-content:center;gap:46px}
.footer-nav a{font-family:'Poppins',sans-serif;font-size:15px;color:var(--white);text-decoration:none}
.footer-contact{position:absolute;left:0;top:3166px;width:1200px;display:flex;justify-content:center;align-items:center;font-family:'Poppins',sans-serif;font-size:16px;color:var(--white)}
.footer-contact .item{display:flex;align-items:center;gap:10px;padding:0 18px}
.footer-contact .divider{width:1px;height:40px;background:#888}
.social{position:absolute;left:0;top:3229px;width:1200px;display:flex;justify-content:center;gap:12px}
.social span{width:30px;height:30px;border-radius:50%;background:var(--white)}
.social span.active{background:var(--light-blue)}
.copyright{position:absolute;left:0;top:3326px;width:1200px;text-align:center;font-family:'Poppins',sans-serif;font-size:13px;color:var(--white)}
</style>
</head>
<body>

<svg class="backdrop" viewBox="0 0 1200 3360" aria-hidden="true">
  <defs>
    <linearGradient id="heroFill" x1="0" y1="0" x2="1" y2="1">
      <stop offset="0" stop-color="#4d6a86"/>
      <stop offset=".45" stop-color="#7f97ad"/>
      <stop offset=".75" stop-color="#2d5f9c"/>
      <stop offset="1" stop-color="#8a9aa8"/>
    </linearGradient>
    <linearGradient id="heroShade" x1="0" y1="0" x2="1" y2="0">
      <stop offset="0" stop-color="#0f2438" stop-opacity=".65"/>
      <stop offset=".55" stop-color="#0f2438" stop-opacity=".15"/>
      <stop offset="1" stop-color="#0f2438" stop-opacity="0"/>
    </linearGradient>
  </defs>
  <g role="img" aria-label="Modern self storage facility with rows of blue roll-up doors under a bright sky">
    <polygon points="0,91 1200,91 1200,640 700,690 0,640" fill="url(#heroFill)"/>
    <polygon points="0,91 1200,91 1200,640 700,690 0,640" fill="url(#heroShade)"/>
  </g>
  <polygon points="0,640 700,690 1200,640 1200,654 700,702 0,654" fill="#1f8fd0"/>
  <!-- projects band -->
  <polygon points="0,1282 600,1350 1200,1282 1200,2440 0,2390" fill="var(--charcoal)"/>
  <polygon points="0,1282 600,1350 1200,1282 1200,1296 600,1364 0,1296" fill="var(--light-blue)"/>
  <polygon points="0,2358 1200,2410 1200,2430 0,2378" fill="var(--light-blue)"/>
  <!-- footer -->
  <polygon points="0,2896 600,2944 1200,2896 1200,3360 0,3360" fill="var(--charcoal)"/>
  <polygon points="0,2884 600,2932 1200,2884 1200,2896 600,2944 0,2896" fill="var(--light-blue)"/>
  <rect x="0" y="3320" width="1200" height="40" fill="var(--charcoal-deep)"/>
</svg>

<header class="site-header">
  <a class="brand" style="left:113px;top:30px"><span class="brand-mark"></span>Kestrel Bay Warehousing Group</a>
  <nav class="main-nav">
    <a class="active" style="left:512px">HOME</a>
    <a style="left:603px">ABOUT US</a>
    <a style="left:724px">SERVICES</a>
    <a style="left:839px">CONTACT</a>
  </nav>
  <a class="btn" style="left:954px;top:22px;width:133px;height:50px">LET’S TALK</a>
</header>

<section class="hero">
  <h1 class="abs hero-title">From Concept to Capacity – Your Self Storage Experts</h1>
  <p class="abs hero-text">Kestrel Bay Warehousing Group delivers turnkey design, construction, leasing, and management services for profitable self storage operations.</p>
  <a class="btn" style="left:113px;top:503px;width:139px;height:49px">GET STARTED</a>
</section>

<section class="services">
  <p class="eyebrow" style="top:772px">OUR EXPERTISE</p>
  <h2 class="section-title" style="top:790px"><span class="accent">Our</span> Services</h2>

  <article class="service-card active" style="left:113px">
    <div class="service-icon">
      <svg width="48" height="40" viewBox="0 0 48 40" fill="none" stroke="#1f9bd7" stroke-width="2"><path d="M6 36V14L24 4l18 10v22"/><path d="M16 36V22h16v14M4 36h40"/></svg>
    </div>
    <h3>Facility Design &amp;<br>Development</h3>
    <p>Smart site selection, market analysis, and architectural planning to maximize project potential.</p>
  </article>
  <article class="service-card" style="left:458px">
    <div class="service-icon">
      <svg width="48" height="40" viewBox="0 0 48 40" fill="none" stroke="#fff" stroke-width="2"><path d="M10 36V20a14 14 0 0 1 28 0v16M6 36h36M24 6v12"/><circle cx="24" cy="26" r="4"/></svg>
    </div>
    <h3>Construction &amp; Build<br>Management</h3>
    <p>Smart site selection, market analysis, and architectural planning to maximize project potential.</p>
  </article>
  <article class="service-card" style="left:799px">
    <div class="service-icon">
      <svg width="44" height="44" viewBox="0 0 44 44" fill="none" stroke="#fff" stroke-width="2"><circle cx="22" cy="22" r="8"/><path d="M22 4v6M22 34v6M4 22h6M34 22h6M9 9l4 4M31 31l4 4M9 35l4-4M31 13l4-4"/></svg>
    </div>
    <h3>Ongoing Facility<br>Management</h3>
    <p>Smart site selection, market analysis, and architectural planning to maximize project potential.</p>
  </article>

  <a class="btn" style="left:529px;top:1235px;width:139px;height:49px">LEARN MORE</a>
</section>

<section class="projects">
  <p class="eyebrow" style="top:1436px;color:var(--white)">OUR WORK</p>
  <h2 class="section-title" style="top:1455px;color:var(--white)"><span class="accent">Featured</span> Projects</h2>

  <article class="project-card" style="left:121px;top:1562px">
    <div class="project-photo" role="img" aria-label="Indoor climate-controlled storage hallway with red unit doors" style="background:linear-gradient(120deg,#b3232b 0%,#c84a45 35%,#d9cdb8 65%,#b9aa94 100%)"></div>
    <div class="project-details"><div class="frame">
      <h4>Aspen Ridge Storage – Edmonton, AB</h4>
      <ul>
        <li>→ Size : 65,000 sq. ft.</li>
        <li>→ Units : 450 climate-controlled</li>
        <li>→ Lease-Up : 90% occupancy within 12 months</li>
        <li>→ Highlight : Designed, built, and managed as</li>
      </ul>
    </div></div>
  </article>

  <article class="project-card" style="left:610px;top:1562px">
    <div class="project-photo" role="img" aria-label="Storage building with orange roll-up doors at sunset" style="background:linear-gradient(180deg,#a07a6a 0%,#c9c6c2 35%,#d4431e 60%,#2d2d2d 100%)"></div>
    <div class="project-label">Coulee Park Storage – Calgary, AB <span>→</span></div>
  </article>

  <article class="project-card" style="left:121px;top:1906px">
    <div class="project-photo" role="img" aria-label="Container-style storage facility with orange units beside a tree" style="background:linear-gradient(110deg,#2c3d55 0%,#b8471c 40%,#d87a2c 60%,#6e8a9a 100%)"></div>
    <div class="project-label">Harbourline Storage – Vancouver, BC <span>→</span></div>
  </article>

  <article class="project-card" style="left:610px;top:1906px">
    <div class="project-photo" role="img" aria-label="Row of orange storage doors along a dark metal building at dusk" style="background:linear-gradient(110deg,#c55a1c 0%,#8b4a2a 40%,#3f4650 65%,#a6b4c4 100%)"></div>
    <div class="project-label">Birchfield Storage – Toronto, ON <span>→</span></div>
  </article>

  <a class="btn" style="left:484px;top:2291px;width:228px;height:48px">SEE MORE PROJECTS</a>
</section>

<section class="contact-banner">
  <p class="eyebrow" style="top:2520px">CONTACT US</p>
  <h2 class="abs cta-title"><span class="accent">Ready to build your</span> next self storage<br>project? Let’s talk.</h2>
  <p class="abs cta-text">Partner with Kestrel Bay Warehousing Group for turnkey development, construction,<br>lease-up, and management expertise.</p>
  <a class="btn" style="left:520px;top:2784px;width:158px;height:49px">CONTACT US</a>
</section>

<footer class="site-footer">
  <a class="brand" style="left:0;top:3006px;width:1200px;justify-content:center;color:var(--white);font-size:24px"><span class="brand-mark" style="width:30px;height:30px"></span>Kestrel Bay Warehousing Group</a>
  <div class="footer-rule" style="top:3080px"></div>
  <nav class="footer-nav">
    <a>HOME</a><a>ABOUT US</a><a>SERVICES</a><a>CONTACT</a>
  </nav>
  <div class="footer-rule" style="top:3136px"></div>
  <div class="footer-contact">
    <div class="item">
      <svg width="18" height="24" viewBox="0 0 18 24"><path d="M9 0a9 9 0 0 1 9 9c0 7-9 15-9 15S0 16 0 9a9 9 0 0 1 9-9z" fill="#2baadf"/><circle cx="9" cy="9" r="3.5" fill="#fff"/></svg>
      10458 82 Ave, Edmonton, AB T6E 2K9
    </div>
    <span class="divider"></span>
    <div class="item">
      <svg width="24" height="16" viewBox="0 0 24 16"><rect width="24" height="16" rx="2" fill="#fff"/><path d="M1 1l11 8 11-8" fill="none" stroke="#3a3a3a" stroke-width="1.6"/></svg>
      info@kestrelbaywarehousing.com
    </div>
    <span class="divider"></span>
    <div class="item">
      <svg width="22" height="22" viewBox="0 0 22 22" fill="none" stroke="#fff" stroke-width="1.6"><circle cx="11" cy="11" r="9.5"/><ellipse cx="11" cy="11" rx="4.5" ry="9.5"/><path d="M1.5 11h19M3 6h16M3 16h16"/></svg>
      www.kestrelbaywarehousing.com
    </div>
  </div>
  <div class="social" aria-label="Social links">
    <span class="active"></span><span></span><span></span><span></span>
  </div>
  <p class="copyright">© Kestrel Bay Warehousing Group – All Rights Reserved | Privacy Policy</p>
</footer>

</body>
</html>
```